Testosterone clinic billboard

Design billboard for Male Testosterone therapy simple to the point but eye catching.
Contact info for the billboard - Vantoraclinic.com
Phone - 555-274-6180

Target Market(s)

Males with disposable income

Industry/Entity Type

medical

Requirements
Must have
• Testosterone Therapy, Erectile Dysfunction, Male Enhancement
Nice to have
• Simple, easy to read

```html
<!DOCTYPE html>
<html lang="en">
<head>
<meta charset="utf-8">
<title>Male Testosterone Therapy Billboard</title>
<link href="https://fonts.googleapis.com/css2?family=Poppins:wght@700;800&display=swap" rel="stylesheet">
<style>
  :root {
    --backdrop: #a6a6a6;
    --purple: #6a2282;
    --charcoal: #454545;
    --teal: #075d60;
    --white: #ffffff;
    --panel: #f3f2f4;
    --photo-light: #ece6e8;
    --photo-rose: #d9a3aa;
    --photo-deep: #a85a66;
  }
  * { margin: 0; padding: 0; box-sizing: border-box; }
  html, body {
    width: 1200px;
    height: 850px;
    overflow: hidden;
    background: var(--backdrop);
    font-family: "Poppins", sans-serif;
  }
  .billboard {
    position: absolute;
    left: 69px;
    top: 225px;
    width: 1050px;
    height: 399px;
    overflow: hidden;
    box-shadow: 0 6px 10px rgba(0,0,0,0.18);
  }
  .hero-photo {
    position: absolute;
    inset: 0;
    background:
      radial-gradient(ellipse 32% 70% at 62% 35%, var(--photo-deep) 0%, rgba(168,90,102,0.35) 45%, rgba(168,90,102,0) 75%),
      radial-gradient(ellipse 40% 80% at 70% 75%, rgba(120,110,115,0.55) 0%, rgba(120,110,115,0) 70%),
      linear-gradient(100deg, var(--photo-light) 0%, #efe3e5 45%, var(--photo-rose) 70%, var(--photo-light) 100%);
  }
  .accent-bar {
    position: absolute;
    left: 756px;
    top: 0;
    width: 294px;
    height: 21px;
    background: var(--purple);
    border-bottom-left-radius: 14px;
  }
  .title-band {
    position: absolute;
    left: 0;
    top: 32px;
    width: 686px;
    height: 45px;
    background: rgba(255,255,255,0.55);
    border-radius: 0 16px 16px 0;
  }
  .title {
    position: absolute;
    left: 41px;
    top: 27px;
    font-weight: 800;
    font-size: 40px;
    line-height: 54px;
    letter-spacing: -0.5px;
    color: var(--charcoal);
    white-space: nowrap;
  }
  .title .accent { color: var(--purple); }
  .info-panel {
    position: absolute;
    left: 0;
    top: 0;
    width: 440px;
    height: 399px;
  }
  .contact {
    position: absolute;
    left: 41px;
    top: 176px;
    color: var(--white);
    font-weight: 700;
    font-size: 27px;
    line-height: 33px;
    white-space: nowrap;
  }
  .benefits {
    position: absolute;
    left: 41px;
    top: 262px;
    list-style: none;
    color: var(--white);
    font-weight: 800;
    font-size: 15px;
    line-height: 23px;
    letter-spacing: -0.2px;
    white-space: nowrap;
  }
  .brand-box {
    position: absolute;
    left: 838px;
    top: 300px;
    width: 212px;
    height: 56px;
    background: var(--panel);
    border-radius: 12px 0 0 12px;
    display: flex;
    align-items: center;
    gap: 8px;
    padding-left: 10px;
  }
  .brand-dot {
    width: 18px;
    height: 18px;
    border-radius: 50%;
    background: var(--teal);
  }
  .brand-name {
    font-weight: 700;
    font-size: 22px;
    color: var(--teal);
  }
</style>
</head>
<body>
  <div class="billboard">
    <div class="hero-photo" role="img" aria-label="Muscular man seen from behind flexing both arms, overlaid with a faint testosterone molecule structure diagram in warm red tones"></div>
    <div class="accent-bar"></div>
    <div class="title-band"></div>
    <h1 class="title"><span class="accent">MALE</span> TESTOSTERONE <span class="accent">THERAPY</span></h1>

    <svg class="info-panel" viewBox="0 0 440 399" aria-hidden="true">
      <path d="M0 181 L318 100 Q362 89 378 141 L438 399 L0 399 Z" fill="var(--teal)"/>
    </svg>

    <div class="contact">
      <p>VANTORACLINIC.COM</p>
      <p>PHONE - 555-274-6180</p>
    </div>

    <ul class="benefits">
      <li>IMROVE FAT DISTRIBUTION.</li>
      <li>IMROVE MUSCLE STRENGTH AND MASS.</li>
      <li>IMROVE FACIAL AND BODY HAIR.</li>
      <li>IMROVE RED BLOOD CELL PRODUCTION.</li>
      <li>IMROVE SEX DRIVE.</li>
    </ul>

    <div class="brand-box">
      <span class="brand-dot"></span>
      <span class="brand-name">Vantoraclinic</span>
    </div>
  </div>
</body>
</html>
```